Free Charity Events from KORVAPLAY

The purpose of the landing page is to get all visitors excited about playing in our Free $500 Charity Tournaments. The visitors who click on the landing page will receive 3 free entries into 3 different $500 Charity Tournaments. A $500 Blackjack Tournament, a $500 Texas Holdem Tournament, and a $500 Baccarat Tournament.

We also offer Free Qualifying games 24/7, where players can earn additional entries into our real paying tournaments.

We will reward the winners in each tournament with a share of the $500 and we will reward a worthy cause or charity with $500 as well.

The money comes from advertising shown during the qualifying game.

Our website is currently being developed on our teams development server. Here is a private link to the site. https://dev.korvaplay.example Attached are vector images of our logo.

Also attached are two attempts we made at a landing page.

Target Market(s)

Social Game Players

Industry/Entity Type

Games

Contact Information for Business Card

The purpose of the business card will be to promote our Free Charity Games. There will be a code hand written on the card. (Meaning we will need a white box to write the code in) If the holder of the card enters that code during registration, they will receive 3 free entries into our real cash tournaments. The giver of the card will receive the affiliate bonus for referring a new player.

Font styles to use
Serif
Sans Serif

Colors
9bcb3c
0292cd
ec1f27

Requirements
Must have
• Excitement, i also like humor but that isn't a must, excitement is.
Nice to have
• Humor
Should not have
• Too many words, we are looking for that image that says at least a few hundred words.

```html
<!DOCTYPE html>
<html lang="en">
<head>
<meta charset="utf-8">
<title>KORVAPLAY – Free Charity Tournaments</title>
<link href="https://fonts.googleapis.com/css2?family=Poppins:wght@300;400;500;600;800&display=swap" rel="stylesheet">
<style>
  :root {
    --backdrop: #383838;
    --paper: #ffffff;
    --frame: #cfcfcf;
    --ink: #2b2b2b;
    --ink-soft: #444444;
    --green: #7aac3a;
    --green-dark: #5f9a2e;
    --red: #d4102a;
    --blue: #2f6fb0;
    --button: #3573b1;
    --icon-line: #777777;
  }
  * { box-sizing: border-box; margin: 0; padding: 0; }
  html, body {
    width: 1200px; height: 1200px; overflow: hidden;
    background: var(--backdrop);
    font-family: "Poppins", sans-serif;
  }
  .landing {
    position: absolute; left: 0; top: 241px;
    width: 1200px; height: 717px;
    background: var(--paper);
    overflow: hidden;
  }
  .hero-photo {
    position: absolute; left: 0; top: 0; width: 1200px; height: 717px;
    background:
      linear-gradient(90deg, #ffffff 0%, rgba(255,255,255,0.92) 40%, rgba(255,255,255,0) 62%),
      linear-gradient(160deg, #ece9e6 0%, #d9d2cc 45%, #b98e6a 70%, #a9a5a2 100%);
  }
  .page-frame {
    position: absolute; left: 12px; top: 13px; width: 1172px; height: 688px;
    border: 1px solid var(--frame);
  }
  .brand {
    position: absolute; left: 75px; top: 68px;
    display: flex; align-items: center; gap: 10px;
  }
  .brand-dot {
    width: 66px; height: 66px; border-radius: 50%;
    background: var(--green);
  }
  .brand-name {
    font-size: 44px; font-weight: 800; color: var(--blue); letter-spacing: 0.5px;
  }
  .social {
    position: absolute; left: 1005px; top: 68px;
    display: flex; gap: 4px;
  }
  .social-link {
    width: 27px; height: 27px; border-radius: 50%;
    border: 1px solid var(--icon-line); background: rgba(255,255,255,0.7);
  }
  .headline { position: absolute; left: 74px; top: 198px; }
  .headline-lead {
    font-size: 55px; font-weight: 300; color: var(--ink); line-height: 62px; letter-spacing: -0.5px;
  }
  .headline-main {
    font-size: 43px; font-weight: 800; color: var(--green); line-height: 50px; letter-spacing: -0.5px;
  }
  .headline-main .prize { color: var(--red); }
  .headline-sub {
    font-size: 29.5px; font-weight: 400; color: var(--blue); line-height: 42px; margin-left: 2px;
  }
  .offer {
    position: absolute; left: 76px; top: 362px;
    display: flex; align-items: center; gap: 10px;
  }
  .offer-free {
    font-size: 58px; font-weight: 800; color: var(--red); line-height: 56px; letter-spacing: -1px;
  }
  .play-now {
    position: relative; width: 290px; height: 48px;
    display: flex; align-items: center; padding-left: 14px;
    font-size: 39px; font-weight: 800; color: #ffffff; letter-spacing: -0.5px;
    text-decoration: none;
  }
  .play-now svg { position: absolute; left: 0; top: 0; z-index: 0; }
  .play-now span { position: relative; z-index: 1; }
  .newsletter { position: absolute; left: 76px; top: 486px; width: 424px; }
  .newsletter-title {
    text-align: center; font-size: 24.5px; font-weight: 400; color: var(--ink-soft); margin-bottom: 16px;
  }
  .email-field {
    height: 48px; border: 1.5px solid #555; border-radius: 4px; background: #fff;
    display: flex; align-items: center; justify-content: center; gap: 10px;
    font-size: 16px; color: #444;
  }
  .subscribe-button {
    margin-top: 9px; height: 48px; border-radius: 4px; background: var(--button);
    display: flex; align-items: center; justify-content: center;
    color: #fff; font-size: 17.5px; font-weight: 600;
  }
</style>
</head>
<body>
  <main class="landing">
    <div class="hero-photo" role="img" aria-label="Excited young woman with long brown hair cheering with a raised fist while looking at her smartphone, on a blurred street background"></div>
    <div class="page-frame"></div>

    <header class="brand">
      <div class="brand-dot"></div>
      <div class="brand-name">KORVAPLAY</div>
    </header>

    <nav class="social" aria-label="Social networks">
      <div class="social-link" aria-label="Social link"></div>
      <div class="social-link" aria-label="Social link"></div>
      <div class="social-link" aria-label="Social link"></div>
      <div class="social-link" aria-label="Social link"></div>
    </nav>

    <section class="headline">
      <h1 class="headline-lead">QUALIFY FOR OUR</h1>
      <p class="headline-main">TOURNAMENTS <span class="prize">$500</span></p>
      <p class="headline-sub">Anytime, Anywhere, Completely</p>
    </section>

    <section class="offer">
      <span class="offer-free">FREE</span>
      <a class="play-now" href="https://dev.korvaplay.example">
        <svg width="290" height="48" viewBox="0 0 290 48" aria-hidden="true">
          <defs>
            <linearGradient id="playGradient" x1="0" y1="0" x2="0" y2="1">
              <stop offset="0" stop-color="#7db43f"/>
              <stop offset="1" stop-color="#5f9a2e"/>
            </linearGradient>
          </defs>
          <polygon points="0,0 274,0 290,24 274,48 0,48" fill="url(#playGradient)"/>
        </svg>
        <span>PLAY NOW</span>
      </a>
    </section>

    <section class="newsletter">
      <p class="newsletter-title">Subscribe to our newsletter</p>
      <div class="email-field">
        <svg width="24" height="17" viewBox="0 0 24 17" aria-hidden="true">
          <rect x="0.5" y="0.5" width="23" height="16" fill="#e9e9e9" stroke="#d5d5d5"/>
          <polyline points="1,1 12,10 23,1" fill="none" stroke="#cfcfcf" stroke-width="1.5"/>
        </svg>
        <span>Enter Your Email</span>
      </div>
      <div class="subscribe-button">SUBSCRIBE</div>
    </section>
  </main>
</body>
</html>
```